Wordpress Template Design using existing Logo and Colors

We are wanting a wordpress theme designing for our b2b marketing consultancy business. A comprehesive and elagant design to our current site www.provexlink.com would be good.

Industry/Entity Type

Marketing

Font styles to use
Sans Serif

```html
<!DOCTYPE html>
<html lang="en">
<head>
<meta charset="utf-8">
<title>Provexlink – B2B Data & Marketing</title>
<link href="https://fonts.googleapis.com/css2?family=Poppins:wght@300;400;500;600;700&display=swap" rel="stylesheet">
<style>
:root{
  --red:#e8212b;
  --ink:#1f2430;
  --text:#5d6370;
  --muted:#8a8f99;
  --nav:#4b5263;
  --slate:#545c6e;
  --pale:#d5d7dd;
  --bg:#ededee;
  --white:#ffffff;
  --footer:#141b27;
  --footer-text:#b7bcc6;
}
*{margin:0;padding:0;box-sizing:border-box}
html,body{width:1200px;height:2993px;overflow:hidden}
body{font-family:'Poppins',sans-serif;color:var(--text);background:var(--bg);position:relative}
.abs{position:absolute}
/* header */
.topbar{left:0;top:0;width:1200px;height:84px;background:var(--white)}
.logo{left:140px;top:22px;display:flex;align-items:center;gap:8px}
.logo-name{font-size:30px;font-weight:700;color:var(--red);letter-spacing:1px;line-height:1}
.logo-dot{width:10px;height:10px;background:var(--red)}
.hq{top:18px;display:flex;align-items:center;gap:10px}
.hq-map{width:72px;height:44px;border-radius:6px}
.hq-label{font-size:10px;color:var(--red);font-weight:500;text-transform:uppercase}
.hq-phone{font-size:14px;color:var(--ink);font-weight:600}
.nav{left:0;top:84px;width:1200px;height:40px;background:var(--nav)}
.nav ul{list-style:none;display:flex;gap:34px;position:absolute;left:142px;top:0;line-height:40px}
.nav li{font-size:11.5px;font-weight:600;color:var(--white);text-transform:uppercase}
.nav-btn{left:884px;top:0;width:183px;height:40px;background:var(--red);color:var(--white);font-size:11.5px;font-weight:600;display:flex;align-items:center;justify-content:center;gap:8px;text-transform:uppercase}
/* hero */
.hero{left:0;top:124px;width:1200px;height:486px;background:linear-gradient(180deg,#b7a891 0%,#c8baa3 35%,#8895a2 70%,#5a5e62 100%)}
.hero-title{left:145px;top:248px;font-size:37px;font-weight:600;color:var(--red);line-height:52px}
.hero-sub{left:147px;top:362px;width:380px;font-size:13px;color:var(--white);line-height:21px}
.hero-btn{left:145px;top:420px;width:122px;height:37px;background:var(--red);color:var(--white);font-size:12px;font-weight:500;display:flex;align-items:center;justify-content:center;text-transform:uppercase}
.hero-dots{left:149px;top:506px;display:flex;gap:14px}
.hero-dots span{width:9px;height:9px;border-radius:50%;background:rgba(255,255,255,.8)}
.hero-dots span.on{background:var(--red);box-shadow:0 0 0 3px rgba(232,33,43,.35)}
.hero-arrow{top:352px;width:24px;height:24px;background:rgba(255,255,255,.35);display:flex;align-items:center;justify-content:center}
/* about */
.about-frame{left:91px;top:660px;width:321px;height:347px;border:5px solid #c9cbd0}
.about-photo{left:189px;top:684px;width:378px;height:294px;background:linear-gradient(135deg,#9fb0c4,#6a7f98 55%,#3d4a5f)}
.about{left:597px;top:688px;width:470px}
.h-sec{font-size:13px;font-weight:600;color:var(--ink);text-transform:uppercase}
.about-tag{font-size:11.5px;color:var(--ink);margin-top:2px}
.rule{width:70px;height:2px;background:var(--red);margin:6px 0 14px}
.about p{font-size:11.2px;line-height:21px;margin-bottom:12px;color:var(--text)}
.feature{top:1031px;height:150px;padding:18px 26px}
.feature h4{font-size:13px;font-weight:600;margin-bottom:8px}
.feature p{font-size:10.5px;line-height:17px}
.f-light{background:var(--pale);color:#4a505c}
.f-light h4{color:var(--ink)}
.f-dark{background:var(--slate);color:#e3e5ea}
.f-dark h4{color:var(--white)}
/* services */
.bgshape{left:0;top:1200px}
.svc-photo{left:0;top:1250px;width:475px;height:560px;background:linear-gradient(180deg,#c9d3e0 0%,#8ea2bb 45%,#4b6589 80%,rgba(237,237,238,0) 100%)}
.services{left:486px;top:1316px;width:570px}
.services .intro{font-size:11.5px;line-height:21px;margin-top:14px}
.svc{width:300px;display:flex;gap:16px}
.svc h5{font-size:11.5px;font-weight:600;color:var(--ink);text-transform:uppercase;margin-bottom:4px}
.svc p{font-size:10.5px;line-height:17px;width:180px}
.team-head{left:620px;top:1772px;width:450px}
.team-head p{font-size:11.2px;line-height:21px;margin-top:8px}
.team-link{font-size:10.5px;color:var(--red);margin-top:4px}
.member{text-align:center}
.member .pic{border-radius:50%;background:radial-gradient(circle at 50% 40%,#d9c3b0,#8c7565 60%,#4a3f3a);margin:0 auto 8px}
.member .pic.ring{box-shadow:0 0 0 8px rgba(232,33,43,.12)}
.member b{display:block;font-size:11.5px;font-weight:600;color:var(--ink)}
.member span{font-size:9.5px;color:var(--muted)}
/* brochure */
.bro-photo{left:924px;top:2452px;width:276px;height:238px;background:linear-gradient(160deg,#e7dccf,#b59a86 55%,#6f5b50)}
.bro{left:198px;top:2530px;width:430px}
.bro p{font-size:11.5px;line-height:22px;margin-top:10px;color:#3f4550}
.bro-btn{left:680px;top:2592px;width:192px;height:37px;border-radius:20px;background:var(--red);color:var(--white);font-size:11.5px;font-weight:600;display:flex;align-items:center;justify-content:center;text-transform:uppercase}
/* footer */
.footer{left:0;top:2690px;width:1200px;height:303px;background:var(--footer)}
.fcol{top:2740px;color:var(--footer-text);font-size:10.5px}
.fcol h6{font-size:11.5px;font-weight:600;color:var(--white);text-transform:uppercase;margin-bottom:4px}
.fcol .u{width:48px;height:2px;background:var(--red);margin-bottom:20px}
.frow{display:flex;gap:14px;align-items:flex-start;margin-bottom:14px;line-height:17px}
.frow svg{flex:none;margin-top:3px}
.fcol p{line-height:17px;margin-bottom:14px}
.fcol .hol{color:var(--red);margin-left:28px}
.news-input{width:192px;height:32px;border:1px solid #3a4252;margin:12px 0;font-size:10px;color:#6a7180;padding:8px 10px}
.news-btn{width:84px;height:26px;background:var(--red);color:var(--white);font-size:10px;font-weight:600;display:flex;align-items:center;justify-content:center;text-transform:uppercase}
.footline{left:0;top:2945px;width:1200px;height:1px;background:#252d3b}
.copy{left:148px;top:2962px;font-size:9.5px;color:#7c8391}
.social{left:928px;top:2958px;display:flex;gap:12px}
.social span{width:16px;height:16px;border-radius:2px;background:#3b5fc4}
.social span.r{background:#e3362e}
.social span.o{background:#e88a24}
</style>
</head>
<body>

<!-- header -->
<div class="abs topbar"></div>
<div class="abs logo"><span class="logo-name">PROVEXLINK</span><span class="logo-dot"></span></div>
<div class="abs hq" style="left:672px">
  <div class="hq-map" role="img" aria-label="United States map in flag colours" style="background:linear-gradient(180deg,#3a4ea0 0 40%,#d8343c 40% 100%)"></div>
  <div><div class="hq-label">Global HQ</div><div class="hq-phone">+1 (555) 014-2290</div></div>
</div>
<div class="abs hq" style="left:888px">
  <div class="hq-map" role="img" aria-label="Singapore map in red" style="background:#dd2a32"></div>
  <div><div class="hq-label">Regional HQ</div><div class="hq-phone">+65 5550 1820</div></div>
</div>

<nav class="abs nav">
  <ul><li>Home</li><li>About Us</li><li>Target Marketing</li><li>Data Management</li><li>Contact Us</li></ul>
</nav>
<div class="abs nav-btn" style="top:84px">
  <svg width="16" height="12" viewBox="0 0 16 12"><path d="M4 11h8a3.5 3.5 0 0 0 0-7 4.5 4.5 0 0 0-8.5 1A3 3 0 0 0 4 11z" fill="none" stroke="#fff" stroke-width="1.4"/></svg>
  Corporate Brochure
</div>

<!-- hero -->
<div class="abs hero" role="img" aria-label="City skyline with a tall broadcast tower at sunset"></div>
<h1 class="abs hero-title">Inbound <span style="display:inline-block;width:16px;height:16px;background:var(--red);vertical-align:middle"></span> Outbound<br>Call Centres</h1>
<p class="abs hero-sub">Attract new leads, increase sales and inspire customers through our in-country call centres network</p>
<div class="abs hero-btn">Learn More</div>
<div class="abs hero-dots"><span class="on"></span><span></span><span></span><span></span></div>
<div class="abs hero-arrow" style="left:80px"><svg width="8" height="10"><path d="M7 1L2 5l5 4" fill="none" stroke="#fff" stroke-width="1.6"/></svg></div>
<div class="abs hero-arrow" style="left:1080px"><svg width="8" height="10"><path d="M1 1l5 4-5 4" fill="none" stroke="#fff" stroke-width="1.6"/></svg></div>
<svg class="abs" style="left:0;top:606px" width="1200" height="36"><polygon points="0,0 660,0 600,32 0,32" fill="#e8212b"/></svg>

<!-- about -->
<div class="abs about-frame"></div>
<div class="abs about-photo" role="img" aria-label="Two colleagues reviewing a document together"></div>
<section class="abs about">
  <h2 class="h-sec">About Provexlink</h2>
  <div class="about-tag">We are a passionate experienced team with big ambitions</div>
  <div class="rule"></div>
  <p>Provexlink is the primary source of market intelligence focused on identifying business opportunities and key decision makers throughout Asia Pacific Region. We provide access to over 3.5 million decision makers across 1.5 million profiled organizations in 23 Asia Pacific countries. With our local presence in 8 countries, we provide tailored target marketing programs in Asia Pacific Region.</p>
  <p>We are a B2B Data, Analytics and Marketing Consulting Company specialized in harnessing the power of potential data to strengthen connections between decisions makers, companies and products. We focus on solutions engineered to solve distinct challenges in the data, direct marketing, and analytics space.</p>
</section>
<div class="abs feature f-light" style="left:434px;width:258px"><h4>Professionals</h4><p>Lorem ipsum dolor sit amet, consectetuer adipiscing elit. Aenean commodo ligula eget dolor. Aenean massa. Cum sociis natoque penatibus et magnis dis parturient montes, nascetur ridiculus mus. Donec</p></div>
<div class="abs feature f-dark" style="left:692px;width:258px"><h4>Trusted</h4><p>Lorem ipsum dolor sit amet, consectetuer adipiscing elit. Aenean commodo ligula eget dolor. Aenean massa. Cum sociis natoque penatibus et magnis dis parturient montes, nascetur ridiculus mus. Donec</p></div>
<div class="abs feature f-light" style="left:950px;width:250px"><h4>Expert services</h4><p>Lorem ipsum dolor sit amet, consectetuer adipiscing elit. Aenean commodo ligula eget dolor. Aenean massa. Cum sociis natoque penatibus et magnis dis parturient montes, nascetur ridiculus mus. Donec</p></div>

<!-- services / team backdrop -->
<svg class="abs bgshape" width="1200" height="1320" viewBox="0 0 1200 1320">
  <path d="M0 90 Q600 -10 1200 70 L1200 1240 Q600 1200 0 1250 Z" fill="#f6f6f7"/>
</svg>
<div class="abs svc-photo" role="img" aria-label="Businessman adjusting his watch over a city skyline"></div>
<section class="abs services">
  <h2 class="h-sec">Our Services</h2>
  <p class="intro">We are a B2B Data, Analytics and Marketing Consulting Company specialized in harnessing the power of potential data to strengthen connections between decisions makers, companies and products. We focus on solutions engineered to solve distinct challenges in the data, direct marketing, and analytics space.</p>
</section>
<div class="abs svc" style="left:464px;top:1466px">
  <svg width="40" height="40" viewBox="0 0 40 40" fill="none" stroke="#e8212b" stroke-width="1.6"><ellipse cx="18" cy="10" rx="12" ry="5"/><path d="M6 10v18c0 3 5 5 12 5M30 10v8M6 19c0 3 5 5 12 5"/><circle cx="30" cy="30" r="6"/></svg>
  <div><h5>B2B Database</h5><p>Get access to Asia's leading market &amp; business intelligence database over 1,500,000 organizations and 3,500,000 decision makers.</p></div>
</div>
<div class="abs svc" style="left:780px;top:1466px">
  <svg width="40" height="40" viewBox="0 0 40 40" fill="none" stroke="#e8212b" stroke-width="1.6"><circle cx="20" cy="20" r="14"/><circle cx="20" cy="16" r="4"/><path d="M12 29c2-5 14-5 16 0M20 2v6M20 32v6M2 20h6M32 20h6"/></svg>
  <div><h5>Target Marketing</h5><p>We develop tailored marketing solutions based on your specific objectives, audience and budget to fetch high returns on investment.</p></div>
</div>
<div class="abs svc" style="left:464px;top:1582px">
  <svg width="40" height="40" viewBox="0 0 40 40" fill="none" stroke="#e8212b" stroke-width="1.6"><path d="M8 22v-4a12 12 0 0 1 24 0v4"/><rect x="5" y="20" width="6" height="10" rx="2"/><rect x="29" y="20" width="6" height="10" rx="2"/><path d="M32 30c0 4-5 6-10 6"/></svg>
  <div><h5>Call Centre</h5><p>When your business requires instantaneous and cost effective contact center, we are here to provide the necessary expertise.</p></div>
</div>
<div class="abs svc" style="left:780px;top:1582px">
  <svg width="40" height="40" viewBox="0 0 40 40" fill="none" stroke="#e8212b" stroke-width="1.6"><rect x="14" y="4" width="12" height="12"/><rect x="4" y="22" width="12" height="12"/><rect x="22" y="22" width="12" height="12"/></svg>
  <div><h5>Data Management</h5><p>We analyze your data and report on effective strategies for turning the data into a profitable resource.</p></div>
</div>

<!-- team -->
<section class="abs team-head">
  <h2 class="h-sec">Our Experienced Team of Experts</h2>
  <p>Our experienced team of data experts are passionate about turning the morass of unstructured data into actionable intelligence. The core team consists of regionally and globally experienced executives and technologycific needs.</p>
  <div class="team-link">Meet Our Team &nbsp;→</div>
</section>
<div class="abs member" style="left:137px;top:1838px;width:160px"><div class="pic" role="img" aria-label="Portrait of team member" style="width:126px;height:126px"></div><b>Dev Harlan</b><span>CEO &amp; Founder</span></div>
<div class="abs member" style="left:400px;top:1888px;width:160px"><div class="pic ring" role="img" aria-label="Portrait of team member" style="width:158px;height:158px"></div><b>Lena Ostrova</b><span>CEO &amp; Founder</span></div>
<div class="abs member" style="left:673px;top:1914px;width:160px"><div class="pic" role="img" aria-label="Portrait of team member" style="width:126px;height:126px"></div><b>Dev Harlan</b><span>CEO &amp; Founder</span></div>
<div class="abs member" style="left:157px;top:2074px;width:160px"><div class="pic" role="img" aria-label="Portrait of team member" style="width:126px;height:126px"></div><b>Dev Harlan</b><span>CEO &amp; Founder</span></div>
<div class="abs member" style="left:860px;top:2048px;width:160px"><div class="pic ring" role="img" aria-label="Portrait of team member" style="width:158px;height:158px"></div><b>Lena Ostrova</b><span>CEO &amp; Founder</span></div>
<div class="abs member" style="left:564px;top:2136px;width:160px"><div class="pic" role="img" aria-label="Portrait of team member" style="width:126px;height:126px"></div><b>Dev Harlan</b><span>CEO &amp; Founder</span></div>
<div class="abs member" style="left:288px;top:2254px;width:160px"><div class="pic" role="img" aria-label="Portrait of team member" style="width:126px;height:126px"></div><b>Dev Harlan</b><span>CEO &amp; Founder</span></div>

<!-- brochure -->
<svg class="abs" style="left:0;top:2430px" width="1200" height="262"><path d="M0 30 Q600 -20 1200 40 L1200 262 L0 262 Z" fill="#e2e2e4"/></svg>
<div class="abs bro-photo" role="img" aria-label="Smiling man wearing glasses"></div>
<section class="abs bro">
  <h2 class="h-sec">Corporate Brochure</h2>
  <p>Learn our leading target marketing and intelligent data management solutions to attain new customers for your niche products and services.Learn our leading target marketing and intelligent data management solutions to attain new customers for your niche products and services.</p>
</section>
<div class="abs bro-btn">Download the Brochure</div>

<!-- footer -->
<svg class="abs" style="left:0;top:2640px" width="1200" height="60"><path d="M0 60 Q600 0 1200 50 L1200 60 Z" fill="#141b27"/></svg>
<footer class="abs footer"></footer>
<div class="abs fcol" style="left:140px;width:210px">
  <h6>Global HQ</h6><div class="u"></div>
  <div class="frow"><svg width="12" height="12" viewBox="0 0 12 12"><path d="M2 1h3l1 3-2 1a7 7 0 0 0 3 3l1-2 3 1v3a1 1 0 0 1-1 1A10 10 0 0 1 1 2a1 1 0 0 1 1-1z" fill="#e8212b"/></svg>+1 (555) 014-2290</div>
  <div class="frow"><svg width="12" height="12" viewBox="0 0 12 12"><rect x="0" y="2" width="12" height="8" fill="#e8212b"/><path d="M0 2l6 4 6-4" fill="none" stroke="#141b27"/></svg>contact.us@provexlink.com</div>
  <div class="frow"><svg width="12" height="12" viewBox="0 0 12 12"><circle cx="6" cy="6" r="5.5" fill="#e8212b"/></svg>www.provexlink.com</div>
  <div class="frow"><svg width="12" height="12" viewBox="0 0 12 12"><path d="M6 0a4 4 0 0 1 4 4c0 3-4 8-4 8S2 7 2 4a4 4 0 0 1 4-4z" fill="#e8212b"/></svg><span>4410 Harbor Crest Way, Suite 210,<br>Oceanview, CA 90010, USA</span></div>
</div>
<div class="abs fcol" style="left:375px;width:220px">
  <h6>Regional HQ</h6><div class="u"></div>
  <div class="frow"><svg width="12" height="12" viewBox="0 0 12 12"><path d="M2 1h3l1 3-2 1a7 7 0 0 0 3 3l1-2 3 1v3a1 1 0 0 1-1 1A10 10 0 0 1 1 2a1 1 0 0 1 1-1z" fill="#e8212b"/></svg>+65 5550 1820</div>
  <div class="frow"><svg width="12" height="12" viewBox="0 0 12 12"><rect x="0" y="2" width="12" height="8" fill="#e8212b"/><path d="M0 2l6 4 6-4" fill="none" stroke="#141b27"/></svg>contact.sg@provexlink.com</div>
  <div class="frow"><svg width="12" height="12" viewBox="0 0 12 12"><circle cx="6" cy="6" r="5.5" fill="#e8212b"/></svg>www.provexlink.com</div>
  <div class="frow"><svg width="12" height="12" viewBox="0 0 12 12"><path d="M6 0a4 4 0 0 1 4 4c0 3-4 8-4 8S2 7 2 4a4 4 0 0 1 4-4z" fill="#e8212b"/></svg><span>18 Meridian Lane, #04-07 Northpoint<br>Hub, Singapore 400118</span></div>
</div>
<div class="abs fcol" style="left:617px;width:200px">
  <h6>Working Hours</h6><div class="u"></div>
  <p>We work weekdays. Please contact us<br>for any enquiry</p>
  <div class="frow"><svg width="12" height="12" viewBox="0 0 12 12"><circle cx="6" cy="6" r="5" fill="none" stroke="#e8212b" stroke-width="1.4"/><path d="M6 3v3l2 1" fill="none" stroke="#e8212b" stroke-width="1.2"/></svg>Monday – Friday : 9AM – 6PM</div>
  <div class="hol" style="margin-top:-8px">Weekends Holiday</div>
</div>
<div class="abs fcol" style="left:850px;width:220px">
  <h6>Newsletter</h6><div class="u"></div>
  <p style="margin-bottom:0">Subscribe to our newsletter for latest<br>updates about our company</p>
  <div class="news-input">Your Email Address</div>
  <div class="news-btn">Subscribe</div>
</div>
<div class="abs footline"></div>
<div class="abs copy">Copyright © 2018 - 2019 Provexlink. All Rights Reserved.</div>
<div class="abs social" aria-label="Social links"><span></span><span></span><span></span><span class="r"></span><span class="o"></span></div>

</body>
</html>
```